Electrician Letterhead Design BLR

We need some letterhead for our bills and other papers.
Customer address is on the right side (Swiss format)
A4 format

Design should also be applicable on Cards

Target Market(s)

Private Customers, Small Business

Industry/Entity Type

Electrician

Other font styles liked:
• incised 901

Colors
00AB8E
00BBA5
67D7C9
C6EFE9
E9F9F6

```html
<!DOCTYPE html>
<html lang="en">
<head>
<meta charset="utf-8">
<title>BLR Letterhead</title>
<link href="https://fonts.googleapis.com/css2?family=Open+Sans:wght@400;600;700&display=swap" rel="stylesheet">
<style>
  :root {
    --teal-deep: #00AB8E;
    --teal: #2FA898;
    --teal-bright: #00BBA5;
    --teal-light: #67D7C9;
    --teal-pale: #C6EFE9;
    --teal-mist: #E9F9F6;
    --paper: #FAFAFA;
    --backdrop: #E6E6E6;
    --ink: #3C3C3C;
  }
  * { margin: 0; padding: 0; box-sizing: border-box; }
  html, body {
    width: 1200px; height: 800px; overflow: hidden;
    background: var(--backdrop);
    font-family: "Open Sans", Arial, sans-serif;
  }
  .letterhead {
    position: absolute;
    left: 338px; top: 30px;
    width: 524px; height: 740px;
    background: var(--paper);
    box-shadow: 0 6px 24px rgba(0,0,0,0.12);
    overflow: hidden;
  }
  .brand {
    position: absolute;
    left: 36px; top: 70px;
  }
  .brand-name {
    display: flex; align-items: center; gap: 8px;
    font-weight: 700; font-size: 40px; line-height: 1;
    color: var(--teal-deep);
    letter-spacing: 1px;
  }
  .brand-mark {
    width: 14px; height: 14px;
    background: var(--teal-deep);
  }
  .brand-company {
    margin-top: 6px;
    font-size: 9.5px; font-weight: 600;
    color: var(--ink);
    letter-spacing: 0.3px;
  }
  .contact {
    position: absolute;
    right: 38px; top: 36px;
    list-style: none;
    font-size: 8.5px; color: var(--ink);
    line-height: 1.45;
  }
  .contact li { display: flex; align-items: center; gap: 5px; }
  .contact svg { width: 8px; height: 8px; flex: none; }
  .footer-band {
    position: absolute; left: 0; bottom: 0;
    width: 524px; height: 150px;
  }
  .footer-address {
    position: absolute; left: 0; right: 0; bottom: 30px;
    text-align: center;
    font-size: 11px; color: #FFFFFF;
    letter-spacing: 0.2px;
  }
</style>
</head>
<body>
  <main class="letterhead">
    <header class="brand">
      <div class="brand-name"><span>BLR</span><span class="brand-mark"></span></div>
      <div class="brand-company">Elektrotechnik Berler GmbH</div>
    </header>

    <ul class="contact">
      <li><svg viewBox="0 0 8 8"><circle cx="4" cy="4" r="4" fill="var(--teal-deep)"/><path d="M2.6 2.2l.8-.2.5 1-.5.4a2.6 2.6 0 0 0 1.2 1.2l.4-.5 1 .5-.2.8c-2 .1-3.3-1.2-3.2-3.2z" fill="#fff"/></svg>+01-2345-678120</li>
      <li><svg viewBox="0 0 8 8"><circle cx="4" cy="4" r="4" fill="var(--teal-deep)"/><path d="M2.6 2.2l.8-.2.5 1-.5.4a2.6 2.6 0 0 0 1.2 1.2l.4-.5 1 .5-.2.8c-2 .1-3.3-1.2-3.2-3.2z" fill="#fff"/></svg>+01-2345-678121</li>
      <li><svg viewBox="0 0 8 8"><circle cx="4" cy="4" r="4" fill="var(--teal-deep)"/><rect x="2" y="2.7" width="4" height="2.8" fill="none" stroke="#fff" stroke-width="0.6"/><path d="M2 2.7l2 1.6 2-1.6" fill="none" stroke="#fff" stroke-width="0.6"/></svg>info@berlerelektro.com</li>
      <li><svg viewBox="0 0 8 8"><circle cx="4" cy="4" r="4" fill="var(--teal-deep)"/><circle cx="4" cy="4" r="2" fill="none" stroke="#fff" stroke-width="0.6"/><path d="M2 4h4M4 2v4" stroke="#fff" stroke-width="0.5"/></svg>www.berlerelektro.com</li>
    </ul>

    <svg class="footer-band" viewBox="0 0 524 150" preserveAspectRatio="none" aria-hidden="true">
      <path d="M0 128 C 160 92, 360 72, 524 58 L524 150 L0 150 Z" fill="var(--teal-pale)"/>
      <path d="M0 134 C 170 100, 360 84, 524 68 L524 150 L0 150 Z" fill="var(--teal)"/>
    </svg>
    <p class="footer-address">Suite 102 Street name, State, Zip 2034, Country</p>
  </main>
</body>
</html>
```